New Advertising Company Business Card

A two sided business card. One side with logo only and the other side with my information and maybe my logo again. Looking for something unique and creative, but not too busy. Info would include my name(Marcus Feldon), President, phone number, address, email address, and website. LOGO IS THE BLUE AND WHITE ONE.

Target Market(s)

CEO/VP Level Audience

Industry/Entity Type

Business

Contact Information for Business Card

In Description.

```html
<!DOCTYPE html>
<html lang="en">
<head>
<meta charset="utf-8">
<title>Arcwell Advertising – Business Card</title>
<link rel="stylesheet" href="https://fonts.googleapis.com/css2?family=Montserrat:wght@600;700&family=Nunito+Sans:wght@400&display=swap">
<style>
  :root {
    --backdrop: #5e5e5e;
    --card-light: #ffffff;
    --card-dark: #1e1e1e;
    --ink: #161616;
    --brand-blue: #0a72c2;
    --white: #ffffff;
  }
  * { margin: 0; padding: 0; box-sizing: border-box; }
  html, body {
    width: 1200px; height: 1200px; overflow: hidden;
    background: var(--backdrop);
  }
  .canvas {
    position: relative; width: 1200px; height: 1200px;
  }
  .card {
    position: absolute; left: 180px; width: 840px; height: 470px;
    border-radius: 14px;
  }
  .card--front { top: 90px; background: var(--card-light); }
  .card--back  { top: 640px; background: var(--card-dark); }

  .wordmark {
    font-family: "Montserrat", sans-serif; font-weight: 600;
    display: flex; align-items: center; gap: 16px;
  }
  .wordmark__dot { border-radius: 50%; background: var(--brand-blue); flex: none; }
  .card--front .wordmark {
    position: absolute; left: 58px; top: 188px;
    color: var(--ink); font-size: 32px; line-height: 1.15;
  }
  .card--front .wordmark__dot { width: 34px; height: 34px; }
  .card--back .wordmark {
    position: absolute; left: 0; right: 0; top: 0; bottom: 0;
    justify-content: center; color: var(--white); font-size: 54px;
  }
  .card--back .wordmark__dot { width: 48px; height: 48px; }

  .details {
    position: absolute; left: 423px; top: 60px;
    font-family: "Nunito Sans", sans-serif; color: var(--ink);
  }
  .details__name {
    font-family: "Montserrat", sans-serif; font-weight: 700;
    font-size: 37px; letter-spacing: -0.3px; line-height: 1.1;
  }
  .details__title {
    color: var(--brand-blue); font-size: 25px; line-height: 1.3; margin-top: 2px;
  }
  .details__rule {
    width: 38px; height: 3px; background: var(--ink); margin: 18px 0 34px;
  }
  .contact-list { list-style: none; font-size: 25px; line-height: 33px; }
  .contact-list li { display: flex; align-items: center; gap: 10px; }
  .contact-list svg {
    width: 20px; height: 20px; flex: none;
    fill: none; stroke: var(--brand-blue); stroke-width: 1.6;
    stroke-linecap: round; stroke-linejoin: round;
  }
  .address { font-size: 25px; line-height: 33px; margin-top: 17px; font-style: normal; }
</style>
</head>
<body>
<main class="canvas">
  <section class="card card--front" aria-label="Card front">
    <div class="wordmark">
      <span class="wordmark__dot"></span>
      <span>Arcwell<br>Advertising</span>
    </div>
    <div class="details">
      <h1 class="details__name">Marcus Feldon</h1>
      <p class="details__title">President</p>
      <div class="details__rule"></div>
      <ul class="contact-list">
        <li><svg viewBox="0 0 20 20"><rect x="5" y="1.5" width="10" height="17" rx="1.5"/><line x1="9" y1="15.5" x2="11" y2="15.5"/></svg>(000) 000-0000</li>
        <li><svg viewBox="0 0 20 20"><path d="M4 2.5l3 .5 1.2 3.5-2 1.5a10 10 0 0 0 5.8 5.8l1.5-2 3.5 1.2.5 3c-.3 1.2-1.4 1.8-2.6 1.6A14 14 0 0 1 2.4 5.1C2.2 3.9 2.8 2.8 4 2.5z"/></svg>(000) 000-0000</li>
        <li><svg viewBox="0 0 20 20"><rect x="2" y="4.5" width="16" height="11"/><path d="M2 4.5l8 6.5 8-6.5M2 15.5l6-5.5M18 15.5l-6-5.5"/></svg>marcus.feldon@domain.com</li>
        <li><svg viewBox="0 0 20 20"><path d="M2.5 10L10 3l7.5 7M4.5 8.5V17h4v-4.5h3V17h4V8.5"/></svg>www.domain.com</li>
      </ul>
      <address class="address">418 Linden Park Road<br>Austin, TX 78731</address>
    </div>
  </section>

  <section class="card card--back" aria-label="Card back">
    <div class="wordmark">
      <span class="wordmark__dot"></span>
      <span>Arcwell Advertising</span>
    </div>
  </section>
</main>
</body>
</html>
```